Web Dashboard for manufacturing data

We need a dashboard for website to show statistical information on buttons/cards/tiles. There will be 12 buttons on the screen (laptop, tablet) On these buttons there are several key pieces of information on each button. 1) Largest info is % 0-100%. 2) 4 status colours neutral, green, yellow, red. 3) Title- up to 20 characters 4) target here is an example... target=above 90%.- When these buttons are tapped, they take user to more info for that specific data.
1 page

```html
<!DOCTYPE html>
<html lang="en">
<head>
<meta charset="UTF-8">
<title>Manufacturing Dashboard</title>
<link rel="stylesheet" href="https://fonts.googleapis.com/css2?family=Inter:wght@400;500;600&display=swap">
<style>
  :root{
    --page:#ffffff;
    --ink:#1d1d22;
    --ink-soft:#3a3a42;
    --muted:#8a8a92;
    --yellow-bg:#fff6e1;
    --green-bg:#e6f3e2;
    --red-bg:#fde3e3;
    --blue-bg:#e5eaf5;
    --yellow-bar:#efe2c4;
    --yellow-accent:#eaae18;
    --green-bar:#a9da9c;
    --red-bar:#eac3c3;
    --red-accent:#e06c6c;
    --blue-line:#4a5ee8;
    --btn-green:#a9da9c;
    --btn-blue:#7aadf4;
    --btn-yellow:#f2d68b;
    --btn-red:#f8b4b4;
  }
  *{box-sizing:border-box;margin:0;padding:0}
  html,body{width:1200px;height:938px;overflow:hidden;background:var(--page)}
  body{font-family:"Inter",sans-serif;color:var(--ink)}
  .dashboard{
    position:absolute;left:55px;top:104px;
    display:grid;grid-template-columns:repeat(4,247px);grid-auto-rows:214px;
    column-gap:34px;row-gap:44px;
  }
  .tile{position:relative;border-radius:14px;padding:20px 20px 0}
  .tile--yellow{background:var(--yellow-bg)}
  .tile--green{background:var(--green-bg)}
  .tile--red{background:var(--red-bg)}
  .tile--blue{background:var(--blue-bg)}
  .tile__title{font-size:11.5px;font-weight:500;color:var(--ink-soft);line-height:14px}
  .tile__stats{display:flex;justify-content:space-between;align-items:center;margin-top:16px;height:28px}
  .tile__value{font-size:23px;font-weight:500;letter-spacing:1px;line-height:28px}
  .tile__change{font-size:10px;display:flex;align-items:center;gap:5px;color:var(--ink-soft)}
  .tile__target{font-size:9.5px;line-height:12px;color:var(--muted);margin-top:3px}
  .tile__chart{position:absolute;left:20px;bottom:10px;width:207px;height:98px}
  .tile__action{
    position:absolute;left:20px;right:20px;bottom:22px;height:42px;border-radius:21px;
    display:flex;align-items:center;justify-content:space-between;padding:0 6px 0 18px;
    font-size:11px;color:var(--ink);text-decoration:none;
  }
  .tile__action--green{background:var(--btn-green)}
  .tile__action--blue{background:var(--btn-blue)}
  .tile__action--yellow{background:var(--btn-yellow)}
  .tile__action--red{background:var(--btn-red)}
  .tile__arrow{width:31px;height:31px;border-radius:50%;background:#fff;display:flex;align-items:center;justify-content:center}
  .axis{font-family:"Inter",sans-serif;font-size:8.5px;fill:var(--ink-soft);text-anchor:middle}
  .axis--small{font-size:6.5px;fill:var(--muted);text-anchor:start}
</style>
</head>
<body>
<main class="dashboard">

  <!-- Row 1 -->
  <section class="tile tile--yellow">
    <h2 class="tile__title">Views</h2>
    <div class="tile__stats"><span class="tile__value">92%</span><span class="tile__change">+11.02% <svg width="10" height="8" viewBox="0 0 10 8"><path d="M1 7 L4 4 L6 5.5 L9 1.5 M6.5 1.5 H9 V4" fill="none" stroke="#1d1d22" stroke-width="1"/></svg></span></div>
    <p class="tile__target">Target: above 90%</p>
    <svg class="tile__chart" viewBox="0 0 207 112">
      <text class="axis axis--small" x="0" y="16">$50</text>
      <text class="axis axis--small" x="0" y="60">$30</text>
      <text class="axis axis--small" x="0" y="104">$10</text>
      <g fill="var(--yellow-bar)">
        <rect x="24" y="60" width="12" height="42"/><rect x="41" y="44" width="12" height="58"/>
        <rect x="58" y="56" width="12" height="46"/><rect x="75" y="70" width="12" height="32"/>
        <rect x="92" y="64" width="12" height="38"/><rect x="109" y="58" width="12" height="44"/>
        <rect x="143" y="60" width="12" height="42"/><rect x="160" y="50" width="12" height="52"/>
        <rect x="177" y="58" width="12" height="44"/>
      </g>
      <rect x="126" y="40" width="12" height="62" fill="var(--yellow-accent)"/>
      <polyline points="30,66 47,52 64,70 81,74 98,64 115,80 132,50 149,76 166,66 183,78" fill="none" stroke="var(--yellow-accent)" stroke-width="1.3"/>
      <g fill="#fff"><circle cx="30" cy="66" r="1.8"/><circle cx="47" cy="52" r="1.8"/><circle cx="64" cy="70" r="1.8"/><circle cx="81" cy="74" r="1.8"/><circle cx="98" cy="64" r="1.8"/><circle cx="115" cy="80" r="1.8"/><circle cx="132" cy="50" r="1.8"/><circle cx="149" cy="76" r="1.8"/><circle cx="166" cy="66" r="1.8"/><circle cx="183" cy="78" r="1.8"/></g>
      <rect x="104" y="8" width="82" height="28" rx="3" fill="#fff" stroke="#eee"/>
      <circle cx="116" cy="22" r="6" fill="var(--yellow-accent)"/>
      <text x="127" y="19" font-size="7" font-weight="600" fill="#1d1d22" font-family="Inter,sans-serif">20 views</text>
      <text x="127" y="29" font-size="5.5" fill="#8a8a92" font-family="Inter,sans-serif">Monday, April 22nd</text>
    </svg>
  </section>

  <section class="tile tile--green">
    <h2 class="tile__title">Visits</h2>
    <div class="tile__stats"><span class="tile__value">87%</span><span class="tile__change">-0.03% <svg width="10" height="8" viewBox="0 0 10 8"><path d="M1 1 L4 4 L6 2.5 L9 6.5 M6.5 6.5 H9 V4" fill="none" stroke="#1d1d22" stroke-width="1"/></svg></span></div>
    <p class="tile__target">Target: above 85%</p>
    <svg class="tile__chart" viewBox="0 0 207 112">
      <g fill="var(--green-bar)">
        <rect x="2" y="52" width="22" height="38"/><rect x="31" y="18" width="22" height="72"/>
        <rect x="60" y="64" width="22" height="26"/><rect x="89" y="6" width="22" height="84"/>
        <rect x="118" y="24" width="22" height="66"/><rect x="147" y="60" width="22" height="30"/>
        <rect x="176" y="48" width="22" height="42"/>
      </g>
      <text class="axis" x="13" y="106">M</text><text class="axis" x="42" y="106">T</text><text class="axis" x="71" y="106">W</text><text class="axis" x="100" y="106">T</text><text class="axis" x="129" y="106">F</text><text class="axis" x="158" y="106">S</text><text class="axis" x="187" y="106">Today</text>
    </svg>
  </section>

  <section class="tile tile--red">
    <h2 class="tile__title">New Users</h2>
    <div class="tile__stats"><span class="tile__value">64%</span><span class="tile__change">+15.03% <svg width="10" height="8" viewBox="0 0 10 8"><path d="M1 7 L4 4 L6 5.5 L9 1.5 M6.5 1.5 H9 V4" fill="none" stroke="#1d1d22" stroke-width="1"/></svg></span></div>
    <p class="tile__target">Target: above 80%</p>
    <svg class="tile__chart" viewBox="0 0 207 112">
      <g fill="var(--red-bar)">
        <rect x="8" y="46" width="14" height="44" rx="7"/><rect x="37" y="14" width="14" height="76" rx="7"/>
        <rect x="66" y="64" width="14" height="26" rx="7"/><rect x="95" y="2" width="14" height="88" rx="7"/>
        <rect x="153" y="28" width="14" height="62" rx="7"/><rect x="182" y="28" width="14" height="62" rx="7"/>
      </g>
      <rect x="124" y="26" width="14" height="64" rx="7" fill="var(--red-accent)"/>
      <text x="131" y="20" font-size="8.5" font-weight="600" fill="var(--red-accent)" text-anchor="middle" font-family="Inter,sans-serif">100</text>
      <text class="axis" x="15" y="106">M</text><text class="axis" x="44" y="106">T</text><text class="axis" x="73" y="106">W</text><text class="axis" x="102" y="106">T</text><text class="axis" x="131" y="106">F</text><text class="axis" x="160" y="106">S</text><text class="axis" x="189" y="106">S</text>
    </svg>
  </section>

  <section class="tile tile--blue">
    <h2 class="tile__title">Active Users</h2>
    <div class="tile__stats"><span class="tile__value">95%</span><span class="tile__change">+6.08% <svg width="10" height="8" viewBox="0 0 10 8"><path d="M1 7 L4 4 L6 5.5 L9 1.5 M6.5 1.5 H9 V4" fill="none" stroke="#1d1d22" stroke-width="1"/></svg></span></div>
    <p class="tile__target">Target: above 90%</p>
    <svg class="tile__chart" viewBox="0 0 207 112">
      <defs><linearGradient id="areaFillA" x1="0" y1="0" x2="0" y2="1"><stop offset="0" stop-color="#7d88f0" stop-opacity=".75"/><stop offset="1" stop-color="#dfe3f8" stop-opacity=".2"/></linearGradient></defs>
      <rect x="126" y="0" width="38" height="86" fill="#f4f6fc" opacity=".9"/>
      <g stroke="#cfd5e6" stroke-width=".6"><line x1="40" y1="10" x2="40" y2="86"/><line x1="80" y1="10" x2="80" y2="86"/><line x1="186" y1="10" x2="186" y2="86"/></g>
      <path d="M0 20 C15 16 25 24 40 22 S62 12 78 24 S100 14 118 18 S135 32 145 26 S165 20 176 28 S195 6 207 24 L207 86 L0 86 Z" fill="url(#areaFillA)"/>
      <path d="M0 20 C15 16 25 24 40 22 S62 12 78 24 S100 14 118 18 S135 32 145 26 S165 20 176 28 S195 6 207 24" fill="none" stroke="var(--blue-line)" stroke-width="1.2"/>
      <text x="145" y="12" font-size="8.5" font-weight="600" fill="var(--blue-line)" text-anchor="middle" font-family="Inter,sans-serif">4500</text>
      <circle cx="145" cy="26" r="4" fill="var(--blue-line)" stroke="#fff" stroke-width="1.2"/>
      <text class="axis" x="6" y="104">10</text><text class="axis" x="40" y="104">11</text><text class="axis" x="80" y="104">12</text><text class="axis" x="115" y="104">13</text><text class="axis" x="145" y="104">14</text><text class="axis" x="186" y="104">15</text>
    </svg>
  </section>

  <!-- Row 2 -->
  <section class="tile tile--green">
    <h2 class="tile__title">Growth</h2>
    <div class="tile__stats"><span class="tile__value">91%</span><span class="tile__change">+11.02% <svg width="10" height="8" viewBox="0 0 10 8"><path d="M1 7 L4 4 L6 5.5 L9 1.5 M6.5 1.5 H9 V4" fill="none" stroke="#1d1d22" stroke-width="1"/></svg></span></div>
    <p class="tile__target">Target: above 90%</p>
    <a class="tile__action tile__action--green" href="#">View Data<span class="tile__arrow"><svg width="14" height="12" viewBox="0 0 14 12"><path d="M1 6 H13 M8 1 L13 6 L8 11" fill="none" stroke="#1d1d22" stroke-width="1.4"/></svg></span></a>
  </section>

  <section class="tile tile--blue">
    <h2 class="tile__title">Today Manufacture</h2>
    <div class="tile__stats"><span class="tile__value">78%</span><span class="tile__change">-0.03% <svg width="10" height="8" viewBox="0 0 10 8"><path d="M1 1 L4 4 L6 2.5 L9 6.5 M6.5 6.5 H9 V4" fill="none" stroke="#1d1d22" stroke-width="1"/></svg></span></div>
    <p class="tile__target">Target: above 75%</p>
    <a class="tile__action tile__action--blue" href="#">View Data<span class="tile__arrow"><svg width="14" height="12" viewBox="0 0 14 12"><path d="M1 6 H13 M8 1 L13 6 L8 11" fill="none" stroke="#1d1d22" stroke-width="1.4"/></svg></span></a>
  </section>

  <section class="tile tile--yellow">
    <h2 class="tile__title">Total Profit</h2>
    <div class="tile__stats"><span class="tile__value">83%</span><span class="tile__change">+15.03% <svg width="10" height="8" viewBox="0 0 10 8"><path d="M1 7 L4 4 L6 5.5 L9 1.5 M6.5 1.5 H9 V4" fill="none" stroke="#1d1d22" stroke-width="1"/></svg></span></div>
    <p class="tile__target">Target: above 90%</p>
    <a class="tile__action tile__action--yellow" href="#">View Data<span class="tile__arrow"><svg width="14" height="12" viewBox="0 0 14 12"><path d="M1 6 H13 M8 1 L13 6 L8 11" fill="none" stroke="#1d1d22" stroke-width="1.4"/></svg></span></a>
  </section>

  <section class="tile tile--red">
    <h2 class="tile__title">Total Expense</h2>
    <div class="tile__stats"><span class="tile__value">46%</span><span class="tile__change">+6.08% <svg width="10" height="8" viewBox="0 0 10 8"><path d="M1 7 L4 4 L6 5.5 L9 1.5 M6.5 1.5 H9 V4" fill="none" stroke="#1d1d22" stroke-width="1"/></svg></span></div>
    <p class="tile__target">Target: below 40%</p>
    <a class="tile__action tile__action--red" href="#">View Data<span class="tile__arrow"><svg width="14" height="12" viewBox="0 0 14 12"><path d="M1 6 H13 M8 1 L13 6 L8 11" fill="none" stroke="#1d1d22" stroke-width="1.4"/></svg></span></a>
  </section>

  <!-- Row 3 -->
  <section class="tile tile--blue">
    <h2 class="tile__title">Total Income</h2>
    <div class="tile__stats"><span class="tile__value">97%</span><span class="tile__change">+6.08% <svg width="10" height="8" viewBox="0 0 10 8"><path d="M1 7 L4 4 L6 5.5 L9 1.5 M6.5 1.5 H9 V4" fill="none" stroke="#1d1d22" stroke-width="1"/></svg></span></div>
    <p class="tile__target">Target: above 90%</p>
    <svg class="tile__chart" viewBox="0 0 207 112">
      <defs><linearGradient id="areaFillB" x1="0" y1="0" x2="0" y2="1"><stop offset="0" stop-color="#7d88f0" stop-opacity=".75"/><stop offset="1" stop-color="#dfe3f8" stop-opacity=".2"/></linearGradient></defs>
      <rect x="126" y="0" width="38" height="86" fill="#f4f6fc" opacity=".9"/>
      <g stroke="#cfd5e6" stroke-width=".6"><line x1="40" y1="10" x2="40" y2="86"/><line x1="80" y1="10" x2="80" y2="86"/><line x1="186" y1="10" x2="186" y2="86"/></g>
      <path d="M0 20 C15 16 25 24 40 22 S62 12 78 24 S100 14 118 18 S135 32 145 26 S165 20 176 28 S195 6 207 24 L207 86 L0 86 Z" fill="url(#areaFillB)"/>
      <path d="M0 20 C15 16 25 24 40 22 S62 12 78 24 S100 14 118 18 S135 32 145 26 S165 20 176 28 S195 6 207 24" fill="none" stroke="var(--blue-line)" stroke-width="1.2"/>
      <text x="145" y="12" font-size="8.5" font-weight="600" fill="var(--blue-line)" text-anchor="middle" font-family="Inter,sans-serif">4500</text>
      <circle cx="145" cy="26" r="4" fill="var(--blue-line)" stroke="#fff" stroke-width="1.2"/>
      <text class="axis" x="6" y="104">10</text><text class="axis" x="40" y="104">11</text><text class="axis" x="80" y="104">12</text><text class="axis" x="115" y="104">13</text><text class="axis" x="145" y="104">14</text><text class="axis" x="186" y="104">15</text>
    </svg>
  </section>

  <section class="tile tile--red">
    <h2 class="tile__title">Total Employee</h2>
    <div class="tile__stats"><span class="tile__value">72%</span><span class="tile__change">+15.03% <svg width="10" height="8" viewBox="0 0 10 8"><path d="M1 7 L4 4 L6 5.5 L9 1.5 M6.5 1.5 H9 V4" fill="none" stroke="#1d1d22" stroke-width="1"/></svg></span></div>
    <p class="tile__target">Target: above 85%</p>
    <svg class="tile__chart" viewBox="0 0 207 112">
      <g fill="var(--red-bar)">
        <rect x="8" y="46" width="14" height="44" rx="7"/><rect x="37" y="14" width="14" height="76" rx="7"/>
        <rect x="66" y="64" width="14" height="26" rx="7"/><rect x="95" y="2" width="14" height="88" rx="7"/>
        <rect x="153" y="28" width="14" height="62" rx="7"/><rect x="182" y="28" width="14" height="62" rx="7"/>
      </g>
      <rect x="124" y="26" width="14" height="64" rx="7" fill="var(--red-accent)"/>
      <text x="131" y="20" font-size="8.5" font-weight="600" fill="var(--red-accent)" text-anchor="middle" font-family="Inter,sans-serif">100</text>
      <text class="axis" x="15" y="106">M</text><text class="axis" x="44" y="106">T</text><text class="axis" x="73" y="106">W</text><text class="axis" x="102" y="106">T</text><text class="axis" x="131" y="106">F</text><text class="axis" x="160" y="106">S</text><text class="axis" x="189" y="106">S</text>
    </svg>
  </section>

  <section class="tile tile--green">
    <h2 class="tile__title">Total Project</h2>
    <div class="tile__stats"><span class="tile__value">88%</span><span class="tile__change">-0.03% <svg width="10" height="8" viewBox="0 0 10 8"><path d="M1 1 L4 4 L6 2.5 L9 6.5 M6.5 6.5 H9 V4" fill="none" stroke="#1d1d22" stroke-width="1"/></svg></span></div>
    <p class="tile__target">Target: above 85%</p>
    <svg class="tile__chart" viewBox="0 0 207 112">
      <g fill="var(--green-bar)">
        <rect x="2" y="52" width="22" height="38"/><rect x="31" y="18" width="22" height="72"/>
        <rect x="60" y="64" width="22" height="26"/><rect x="89" y="6" width="22" height="84"/>
        <rect x="118" y="24" width="22" height="66"/><rect x="147" y="60" width="22" height="30"/>
        <rect x="176" y="48" width="22" height="42"/>
      </g>
      <text class="axis" x="13" y="106">M</text><text class="axis" x="42" y="106">T</text><text class="axis" x="71" y="106">W</text><text class="axis" x="100" y="106">T</text><text class="axis" x="129" y="106">F</text><text class="axis" x="158" y="106">S</text><text class="axis" x="187" y="106">Today</text>
    </svg>
  </section>

  <section class="tile tile--yellow">
    <h2 class="tile__title">Total Pending</h2>
    <div class="tile__stats"><span class="tile__value">69%</span><span class="tile__change">+11.02% <svg width="10" height="8" viewBox="0 0 10 8"><path d="M1 7 L4 4 L6 5.5 L9 1.5 M6.5 1.5 H9 V4" fill="none" stroke="#1d1d22" stroke-width="1"/></svg></span></div>
    <p class="tile__target">Target: below 50%</p>
    <svg class="tile__chart" viewBox="0 0 207 112">
      <text class="axis axis--small" x="0" y="16">$50</text>
      <text class="axis axis--small" x="0" y="60">$30</text>
      <text class="axis axis--small" x="0" y="104">$10</text>
      <g fill="var(--yellow-bar)">
        <rect x="24" y="60" width="12" height="42"/><rect x="41" y="44" width="12" height="58"/>
        <rect x="58" y="56" width="12" height="46"/><rect x="75" y="70" width="12" height="32"/>
        <rect x="92" y="64" width="12" height="38"/><rect x="109" y="58" width="12" height="44"/>
        <rect x="143" y="60" width="12" height="42"/><rect x="160" y="50" width="12" height="52"/>
        <rect x="177" y="58" width="12" height="44"/>
      </g>
      <rect x="126" y="40" width="12" height="62" fill="var(--yellow-accent)"/>
      <polyline points="30,66 47,52 64,70 81,74 98,64 115,80 132,50 149,76 166,66 183,78" fill="none" stroke="var(--yellow-accent)" stroke-width="1.3"/>
      <g fill="#fff"><circle cx="30" cy="66" r="1.8"/><circle cx="47" cy="52" r="1.8"/><circle cx="64" cy="70" r="1.8"/><circle cx="81" cy="74" r="1.8"/><circle cx="98" cy="64" r="1.8"/><circle cx="115" cy="80" r="1.8"/><circle cx="132" cy="50" r="1.8"/><circle cx="149" cy="76" r="1.8"/><circle cx="166" cy="66" r="1.8"/><circle cx="183" cy="78" r="1.8"/></g>
    </svg>
  </section>

</main>
</body>
</html>
```